Modern Yoga Studio Timetable and Flyer Design

We have a comprehensive class timetable and we are wanting to a clean modern look for our Spring timetable.

We require a double sided flyer with our class timetable included.
We would prefer an A5 size (postcard) or DL (1/3 A4).

We would like the final flyer to have.
Side A : Yoga image, logo

Fennel Stretch Hall
address: 4/71 Wexcombe Lane, Pelharton
website: fennelstretch.com.au
mobile: 0471 296 814

Side B: Clear easy to read timetable with a break down of class types and website.

We would also like to have a copy of the timetable itself as a separate jpg or pdf for use on our website to download.

Thank you.
Yours kindly,
Nell

I have attached a sample of another timetable of which I like the look and feel of, however this is just a guide. I've also attached our 'new' schedule in WORD plus uploaded our last design of the front.
Updates

Target Market(s)

Women aged 30-45

Industry/Entity Type

Health And Wellness

Font styles to use
Other font styles liked:
• Brandon Grotesque, Jenna Sue

Colors
6c459b
33a6d7
ffffff

Requirements
Must have
• A definitive colour to decipher between different class types on our timetable. Where each colour represents a different class type. Colours and layouts similar to our website design, see www.fennelstretch.com.au
Nice to have
• I've included a design of another studio whose timetable design I like. One of our own yoga images instead of a stock image.
Should not have
• No dark gridlines between the cells/boxes in the timetables. Please don't use stock yoga images.

```html
<!DOCTYPE html>
<html lang="en">
<head>
<meta charset="utf-8">
<title>Fennel Stretch Hall – Spring Flyer</title>
<link rel="stylesheet" href="https://fonts.googleapis.com/css2?family=Open+Sans:wght@300;400;600;700&display=swap">
<style>
  :root{
    --purple:#6c459b;
    --purple-deep:#4a2a86;
    --blue:#33a6d7;
    --white:#ffffff;
    --backdrop:#e4e4e4;
    --cell:#c9c9c9;
    --head-red:#d0201f;
    --time-blue:#3b8fd0;
    --c-rise:#5aae93;
    --c-vinyasa:#3aa3d4;
    --c-yin:#333333;
    --c-slow:#8e1f7d;
    --c-preg:#e08a7a;
    --c-mum:#d45c9c;
    --c-kids-a:#4a9a2e;
    --c-kids-b:#24418f;
    --c-teens:#e0901a;
    --c-flow:#555555;
    --c-yinrest:#8b1a1a;
    --c-women:#7ec4c4;
  }
  *{box-sizing:border-box;margin:0;padding:0}
  html,body{width:1200px;height:803px;overflow:hidden}
  body{background:var(--backdrop);font-family:"Open Sans",Arial,sans-serif;position:relative}
  .flyer{position:absolute;top:29px;width:470px;height:745px;background:var(--white);overflow:hidden;box-shadow:0 2px 8px rgba(0,0,0,.12)}
  .flyer--front{left:60px}
  .flyer--back{left:670px}
  .mandala{position:absolute;left:20px;top:0;width:430px;height:195px;border-radius:0 0 215px 215px / 0 0 195px 195px;
    background:radial-gradient(ellipse at 50% 0%,var(--purple-deep) 0%,var(--purple) 35%,#a889c9 70%,#efe8f6 100%)}
  .brand{position:absolute;top:240px;left:0;width:100%;text-align:center;color:var(--blue);font-weight:300;font-size:34px;letter-spacing:7px}
  .rule{position:absolute;left:0;width:100%;height:3px}
  .rule--blue{background:var(--blue)}
  .rule--purple{background:var(--purple)}
  .photo{position:absolute;left:0;top:342px;width:100%;height:373px;background:linear-gradient(160deg,#d9d3c8 0%,#a6a09a 45%,#4d4a52 100%)}
  .photo-circle{position:absolute;top:210px;width:92px;height:92px;border-radius:50%;border:3px solid var(--purple);background:linear-gradient(150deg,#c9a98c,#7a5c8e)}
  .url-pill{position:absolute;left:162px;top:325px;background:var(--blue);color:var(--white);font-size:17px;padding:2px 12px;border-radius:5px}
  .contact-band{position:absolute;left:0;bottom:0;width:100%;height:30px;background:var(--purple);border-top:3px solid var(--blue)}
  .contact-info{position:absolute;left:80px;right:80px;top:0;height:27px;display:flex;align-items:center;justify-content:center;gap:22px;color:var(--white);font-size:9.5px;font-weight:600;white-space:nowrap}
  .band-arrow{position:absolute;top:9px}
  .band-arrow--left{left:12px}
  .band-arrow--right{right:12px}
  .site-tag{position:absolute;top:318px;right:8px;font-size:7.5px;font-weight:700;color:#333}
  .tt-title{position:absolute;top:350px;width:100%;text-align:center;font-size:8px;font-weight:700;color:var(--blue)}
  .timetable{position:absolute;left:10px;top:365px;width:450px;display:grid;grid-template-columns:60px repeat(7,1fr);grid-template-rows:22px repeat(13,23px);background:var(--cell);column-gap:1px}
  .day{background:var(--head-red);color:var(--white);font-size:8px;font-weight:700;display:flex;align-items:center;justify-content:center;grid-row:1}
  .corner{background:var(--time-blue);grid-row:1;grid-column:1}
  .time{background:var(--time-blue);color:var(--white);font-size:8px;font-weight:700;display:flex;align-items:center;padding-left:8px;grid-column:1;border-top:1px solid var(--white)}
  .class{color:var(--white);font-size:6.5px;font-weight:600;display:flex;align-items:center;justify-content:center;text-align:center;line-height:1.15;margin:2px 0}
  .rise{background:var(--c-rise)} .vinyasa{background:var(--c-vinyasa)} .yin{background:var(--c-yin)}
  .slow{background:var(--c-slow)} .preg{background:var(--c-preg)} .mum{background:var(--c-mum)}
  .kids-a{background:var(--c-kids-a)} .kids-b{background:var(--c-kids-b)} .teens{background:var(--c-teens)}
  .flow{background:var(--c-flow)} .yinrest{background:var(--c-yinrest)} .women{background:var(--c-women)}
  .booking-note{position:absolute;left:10px;top:699px;font-size:8px;font-weight:700;color:#222}
</style>
</head>
<body>
  <section class="flyer flyer--front">
    <div class="mandala" role="img" aria-label="Purple half-mandala ornament across the top"></div>
    <div class="brand">Fennel Stretch Hall</div>
    <div class="rule rule--blue" style="top:333px"></div>
    <div class="rule rule--purple" style="top:337px"></div>
    <div class="photo" role="img" aria-label="Studio interior with mats, bolsters and a yogi in a handstand by the glass door">
      <div class="photo-circle" style="left:88px" role="img" aria-label="Yogi in a twisted side pose"></div>
      <div class="photo-circle" style="left:189px" role="img" aria-label="Hands in prayer holding mala beads"></div>
      <div class="photo-circle" style="left:290px" role="img" aria-label="Yogi in downward dog"></div>
      <div class="url-pill">fennelstretch.com.au</div>
    </div>
    <footer class="contact-band">
      <svg class="band-arrow band-arrow--left" width="56" height="8" viewBox="0 0 56 8"><path d="M0 4H54M48 0L54 4L48 8M2 0L6 4L2 8M8 0L12 4L8 8" stroke="#fff" fill="none" stroke-width="1"/></svg>
      <div class="contact-info">
        <span>Mobile: 0471 296 814</span>
        <span>Address: 4/71 Wexcombe Lane, Pelharton</span>
      </div>
      <svg class="band-arrow band-arrow--right" width="56" height="8" viewBox="0 0 56 8"><path d="M2 4H56M8 0L2 4L8 8M54 0L50 4L54 8M48 0L44 4L48 8" stroke="#fff" fill="none" stroke-width="1"/></svg>
    </footer>
  </section>

  <section class="flyer flyer--back">
    <div class="mandala" role="img" aria-label="Purple half-mandala ornament across the top"></div>
    <div class="brand">Fennel Stretch Hall</div>
    <div class="site-tag">fennelstretch.com.au</div>
    <div class="rule rule--purple" style="top:333px"></div>
    <div class="rule rule--blue" style="top:337px"></div>
    <h2 class="tt-title">FENNEL STRETCH SPRING TIME TABLE</h2>
    <div class="timetable">
      <div class="corner"></div>
      <div class="day" style="grid-column:2">MON</div>
      <div class="day" style="grid-column:3">TUE</div>
      <div class="day" style="grid-column:4">WED</div>
      <div class="day" style="grid-column:5">THU</div>
      <div class="day" style="grid-column:6">FRI</div>
      <div class="day" style="grid-column:7">SAT</div>
      <div class="day" style="grid-column:8">SUN</div>

      <div class="time" style="grid-row:2">5:45 AM</div>
      <div class="time" style="grid-row:3">9:00 AM</div>
      <div class="time" style="grid-row:4">9:15 AM</div>
      <div class="time" style="grid-row:5">9:30 AM</div>
      <div class="time" style="grid-row:6">10:30 AM</div>
      <div class="time" style="grid-row:7">11:00 AM</div>
      <div class="time" style="grid-row:8">12:15 PM</div>
      <div class="time" style="grid-row:9">4:00 PM</div>
      <div class="time" style="grid-row:10">4:45 PM</div>
      <div class="time" style="grid-row:11">5:00 PM</div>
      <div class="time" style="grid-row:12">6:00 PM</div>
      <div class="time" style="grid-row:13">6:15 PM</div>
      <div class="time" style="grid-row:14">7:30 PM</div>

      <div class="class rise" style="grid-column:3;grid-row:2">RISE + SHINE*</div>
      <div class="class rise" style="grid-column:5;grid-row:2">RISE + SHINE*</div>
      <div class="class vinyasa" style="grid-column:7;grid-row:3">VINYASA FLOW</div>
      <div class="class vinyasa" style="grid-column:3;grid-row:4">VINYASA FLOW</div>
      <div class="class yin" style="grid-column:8;grid-row:4">YIN</div>
      <div class="class slow" style="grid-column:2;grid-row:5">SLOW FLOW</div>
      <div class="class vinyasa" style="grid-column:5;grid-row:5">VINYASA FLOW</div>
      <div class="class preg" style="grid-column:7;grid-row:6">PREGNANCY*</div>
      <div class="class mum" style="grid-column:3;grid-row:7">MUM+BABY*</div>
      <div class="class mum" style="grid-column:5;grid-row:7">MUM+BABY*</div>
      <div class="class preg" style="grid-column:5;grid-row:8">PREGNANCY</div>
      <div class="class vinyasa" style="grid-column:7;grid-row:8">VINYASA FLOW</div>
      <div class="class kids-a" style="grid-column:4;grid-row:9">KIDS<br>8-12*</div>
      <div class="class kids-b" style="grid-column:5;grid-row:9">KIDS<br>5-7*</div>
      <div class="class teens" style="grid-column:4;grid-row:10">TEENS<br>12-16*</div>
      <div class="class teens" style="grid-column:5;grid-row:11">TEENS<br>12-16*</div>
      <div class="class flow" style="grid-column:6;grid-row:11">FLOW+RESTORE</div>
      <div class="class preg" style="grid-column:2;grid-row:12">PREGNANCY*</div>
      <div class="class vinyasa" style="grid-column:3;grid-row:12">VINYASA FLOW</div>
      <div class="class slow" style="grid-column:4;grid-row:12">SLOW FLOW</div>
      <div class="class preg" style="grid-column:5;grid-row:13">PREGNANCY*</div>
      <div class="class yinrest" style="grid-column:4;grid-row:14">YIN+RESTORE</div>
      <div class="class women" style="grid-column:5;grid-row:14">WOMEN'S<br>WELLNESS*</div>
    </div>
    <p class="booking-note">*Booking Essential</p>
    <footer class="contact-band">
      <svg class="band-arrow band-arrow--left" width="56" height="8" viewBox="0 0 56 8"><path d="M0 4H54M48 0L54 4L48 8M2 0L6 4L2 8M8 0L12 4L8 8" stroke="#fff" fill="none" stroke-width="1"/></svg>
      <div class="contact-info">
        <span>Mobile: 0471 296 814</span>
        <span>Address: 4/71 Wexcombe Lane, Pelharton</span>
      </div>
      <svg class="band-arrow band-arrow--right" width="56" height="8" viewBox="0 0 56 8"><path d="M2 4H56M8 0L2 4L8 8M54 0L50 4L54 8M48 0L44 4L48 8" stroke="#fff" fill="none" stroke-width="1"/></svg>
    </footer>
  </section>
</body>
</html>
```